KT-Systems advertising flag and billboard design

I need a design for advertising flag and a design for billboard.
Information can be obtained from https://kt-sytronik.de.
Updates
Target Market(s)
IT service for companies
Requirements
Must have
- Logo, contact information and services

```html
<!DOCTYPE html>
<html lang="de">
<head>
<meta charset="utf-8">
<title>KT-Systems – Billboard und Werbeflagge</title>
<link rel="stylesheet" href="https://fonts.googleapis.com/css2?family=League+Spartan:wght@500;700;800&family=Poppins:wght@500;600;700&family=Oswald:wght@600&display=swap">
<style>
  :root {
    --stage: #c4c4c4;
    --navy-deep: #13141f;
    --navy: #181a2c;
    --indigo: #10106a;
    --band: #1b2aa3;
    --accent: #4a7aef;
    --white: #ffffff;
    --tick: #4a7aef;
  }
  * { margin: 0; padding: 0; box-sizing: border-box; }
  html, body { width: 1200px; height: 2189px; overflow: hidden; }
  body { background: var(--stage); position: relative; font-family: "Poppins", sans-serif; }

  /* Billboard */
  .billboard {
    position: absolute; left: 64px; top: 105px; width: 1064px; height: 311px;
    background: linear-gradient(90deg, var(--navy-deep) 0%, var(--navy) 60%, #1c2030 100%);
    overflow: hidden;
  }
  .billboard__photo {
    position: absolute; right: 0; top: 0; width: 400px; height: 100%;
    background: linear-gradient(90deg, rgba(24,26,44,1) 0%, rgba(52,60,78,0.85) 35%, #3a4150 65%, #2b303c 100%);
  }
  .billboard__title-light {
    position: absolute; left: 36px; top: 28px;
    font-family: "League Spartan", sans-serif; font-weight: 500;
    font-size: 80px; line-height: 1; color: var(--accent); letter-spacing: -1px;
  }
  .billboard__title-bold {
    position: absolute; left: 36px; top: 98px;
    font-family: "League Spartan", sans-serif; font-weight: 800;
    font-size: 60px; line-height: 1; color: var(--white); letter-spacing: 0.5px;
  }
  .billboard__band {
    position: absolute; left: 0; top: 157px; width: 820px; height: 72px;
    background: linear-gradient(90deg, var(--band) 0%, var(--band) 70%, rgba(27,42,163,0) 100%);
  }
  .services {
    position: absolute; left: 42px; top: 162px; list-style: none;
    display: grid; grid-template-columns: 232px 219px 230px; row-gap: 6px;
  }
  .services li {
    display: flex; align-items: center; gap: 8px;
    color: var(--white); font-size: 18px; font-weight: 500; line-height: 23px;
  }
  .services svg { width: 15px; height: 15px; flex: none; }
  .billboard__brand {
    position: absolute; left: 38px; top: 247px;
    font-family: "Poppins", sans-serif; font-weight: 700; font-size: 30px;
    color: var(--white); letter-spacing: 2px; display: flex; align-items: center; gap: 10px;
  }
  .brand-dot { width: 16px; height: 16px; background: var(--accent); display: inline-block; }
  .billboard__url {
    position: absolute; left: 444px; top: 250px;
    font-weight: 700; font-size: 27px; color: var(--white);
  }

  /* Flag */
  .flag {
    position: absolute; left: 384px; top: 488px; width: 423px; height: 1587px;
    background: radial-gradient(ellipse 70% 40% at 55% 50%, var(--indigo) 0%, #141538 55%, var(--navy-deep) 100%);
    overflow: hidden;
  }
  .flag svg { position: absolute; left: 0; top: 0; }
  .flag__brand { font-family: "Poppins", sans-serif; font-weight: 700; font-size: 30px; fill: var(--white); letter-spacing: 2px; }
  .flag__title-light { font-family: "League Spartan", sans-serif; font-weight: 500; font-size: 182px; fill: var(--accent); }
  .flag__title-bold { font-family: "League Spartan", sans-serif; font-weight: 800; font-size: 100px; fill: var(--white); }
  .flag__phone { font-family: "Oswald", sans-serif; font-weight: 600; font-size: 66px; fill: var(--white); }
  .flag__url { font-family: "Oswald", sans-serif; font-weight: 600; font-size: 33px; fill: var(--white); }
</style>
</head>
<body>

<section class="billboard" aria-label="Billboard">
  <div class="billboard__photo" role="img" aria-label="Foto: Geschäftsmann im Anzug arbeitet am Laptop, davor leuchtende Netzwerk- und Code-Einblendungen"></div>
  <div class="billboard__band"></div>
  <h1 class="billboard__title-light">IHR LOKALER</h1>
  <h2 class="billboard__title-bold">COMPUTERSPEZIALIST</h2>
  <ul class="services">
    <li><svg viewBox="0 0 16 16"><circle cx="8" cy="8" r="8" fill="var(--tick)"/><path d="M4.5 8.2l2.3 2.3 4.7-4.7" stroke="#fff" stroke-width="2" fill="none"/></svg>Firewall-Lösungen</li>
    <li><svg viewBox="0 0 16 16"><circle cx="8" cy="8" r="8" fill="var(--tick)"/><path d="M4.5 8.2l2.3 2.3 4.7-4.7" stroke="#fff" stroke-width="2" fill="none"/></svg>Antivirensysteme</li>
    <li><svg viewBox="0 0 16 16"><circle cx="8" cy="8" r="8" fill="var(--tick)"/><path d="M4.5 8.2l2.3 2.3 4.7-4.7" stroke="#fff" stroke-width="2" fill="none"/></svg>Hardware Lösungen</li>
    <li><svg viewBox="0 0 16 16"><circle cx="8" cy="8" r="8" fill="var(--tick)"/><path d="M4.5 8.2l2.3 2.3 4.7-4.7" stroke="#fff" stroke-width="2" fill="none"/></svg>E-Mail-Sicherheit</li>
    <li><svg viewBox="0 0 16 16"><circle cx="8" cy="8" r="8" fill="var(--tick)"/><path d="M4.5 8.2l2.3 2.3 4.7-4.7" stroke="#fff" stroke-width="2" fill="none"/></svg>Cloud-Lösungen</li>
    <li><svg viewBox="0 0 16 16"><circle cx="8" cy="8" r="8" fill="var(--tick)"/><path d="M4.5 8.2l2.3 2.3 4.7-4.7" stroke="#fff" stroke-width="2" fill="none"/></svg>Software Lösungen</li>
  </ul>
  <div class="billboard__brand"><span class="brand-dot"></span>KT-SYSTEMS</div>
  <div class="billboard__url">www.kt-sytronik.de</div>
</section>

<section class="flag" aria-label="Werbeflagge">
  <svg width="423" height="1587" viewBox="0 0 423 1587">
    <rect x="96" y="112" width="16" height="16" fill="var(--accent)"/>
    <text class="flag__brand" x="122" y="131">KT-SYSTEMS</text>
    <text class="flag__title-light" transform="translate(232 1263) rotate(-90)" textLength="1088" lengthAdjust="spacingAndGlyphs">IHR LOKALER</text>
    <text class="flag__title-bold" transform="translate(321 1267) rotate(-90)" textLength="1096" lengthAdjust="spacingAndGlyphs">COMPUTERSPEZIALIST</text>
    <text class="flag__phone" x="211" y="1418" text-anchor="middle" textLength="320" lengthAdjust="spacingAndGlyphs">01234-5678910</text>
    <rect x="53" y="1435" width="332" height="54" rx="27" fill="var(--accent)"/>
    <text class="flag__url" x="219" y="1476" text-anchor="middle" textLength="292" lengthAdjust="spacingAndGlyphs">WWW.KT-SYTRONIK.DE</text>
  </svg>
</section>

</body>
</html>
```